依頼詳細
ポスティング用のチラシです。
思わず手に取って見たくなるようなデザインとキャッチャーなコピーを
ご提案ください。

原稿にイラストを入れましたが、写真でも構いません。
また、全体のレイアウトも自由に変更頂いて構いません。

尚、コンペで表面が決まりましたら、裏面に着手していただきますので、
ご承知おきください。

それではご提案お待ちしております。
何卒よろしくお願い申し上げます。

記載項目
原稿にまとめました
サイズ
A4
ページ数
両面
希望イメージ
シンプル 複雑
単色 カラフル
暗い 明るい
日常 高級
遊び心 厳粛
未来的 伝統的
女性的 男性的
希望する色
納品ファイル
• イラストレーター形式 (.ai)
補足説明
お世話様でございます。
どれも素晴らしいご提案、誠にありがとうございました。
検討させていただきますので、決定までにしばらくお時間くださいませ。
宜しくお願い申し上げます。
■ 選んだ理由

インパクトのあるアイキャッチ(イラスト・コピー)と、非常に分かり易くまとめて頂いた所が
ポイントです。

■ 提案者全員のお礼・コメント

この度は素晴らしい作品をご提案頂きまして、誠にありがとうございました。
また機会を作りますので、今後ともよろしくお願い申し上げます。

```html
<!DOCTYPE html>
<html lang="ja">
<head>
<meta charset="utf-8">
<title>Lumo 出張メガネ チラシ</title>
<link rel="stylesheet" href="https://fonts.googleapis.com/css2?family=M+PLUS+Rounded+1c:wght@500;800&family=Noto+Sans+JP:wght@400;700;900&display=swap">
<style>
:root{
  --green:#3ea33a;
  --green-dark:#2a7f2a;
  --green-pale:#e6f3dc;
  --yellow:#ffe84a;
  --text:#333;
  --muted:#666;
  --white:#fff;
  --orange:#e9672a;
}
*{box-sizing:border-box;margin:0;padding:0}
html,body{width:900px;height:1200px;overflow:hidden;background:var(--white)}
body{font-family:"Noto Sans JP",sans-serif;color:var(--text);position:relative}
.abs{position:absolute}
.ph{position:absolute;border-radius:6px}

.eyebrow{left:40px;top:42px;font-size:31px;font-weight:700;color:#555;letter-spacing:2px}
.brand{left:36px;top:78px;font-family:"M PLUS Rounded 1c",sans-serif;font-weight:800;font-size:140px;line-height:1;color:var(--green);letter-spacing:-2px}

.safety{right:28px;top:22px;width:318px;height:196px;border:3px solid var(--green);border-radius:10px;background:var(--white);padding:34px 10px 8px}
.safety-title{position:absolute;left:-3px;right:-3px;top:-3px;background:var(--green);color:var(--white);font-weight:900;font-size:17px;text-align:center;padding:5px 0;border-radius:10px 10px 0 0}
.safety-grid{display:flex;flex-wrap:wrap;justify-content:center;gap:6px 10px}
.safety-item{width:88px;text-align:center;font-size:11px;color:var(--muted)}
.safety-icon{width:52px;height:52px;margin:0 auto 3px;border-radius:50%;background:linear-gradient(#dfeef6,#b9d7e8)}

.couple{left:585px;top:232px;width:290px;height:268px;background:linear-gradient(160deg,#eef1f3,#c9d1d6);border-radius:0}
.bubble{position:absolute;border-radius:50%;background:var(--yellow);display:flex;align-items:center;justify-content:center;text-align:center;font-weight:900;color:var(--text);line-height:1.35}
.bubble.call{left:462px;top:150px;width:124px;height:124px;font-size:15px}
.bubble.eye{left:468px;top:392px;width:124px;height:124px;font-size:14px;background:var(--white);border:3px solid var(--green);color:var(--green-dark)}

.lead{left:40px;top:284px;font-size:26px;font-weight:900;color:var(--green-dark);line-height:1.45}
.interior{top:376px;width:200px;height:100px;background:linear-gradient(150deg,#d9d4c8,#9e978a)}
.interior.a{left:40px}
.interior.b{left:252px}

.band{left:0;top:470px;width:900px;height:120px}
.van{left:610px;top:440px;width:270px;height:150px;background:linear-gradient(160deg,#f4f6f8,#b9c3cb)}

.headline{left:40px;top:598px;font-size:32px;font-weight:900;color:var(--green-dark);line-height:1.45}

.glasses{left:40px;top:712px;width:230px;height:92px;background:linear-gradient(90deg,#e8efe2,#c6d7b9)}
.bubble.deliver{left:282px;top:694px;width:120px;height:120px;font-size:14px;background:var(--white);border:3px solid var(--green);border-radius:50%}
.lens-note{left:40px;top:820px;width:420px;font-size:13.5px;line-height:1.6}
.lens-note b{color:var(--green-dark)}

.free{left:470px;top:706px;width:400px}
.free-list{list-style:none;width:200px}
.free-list li{background:var(--green);color:var(--white);font-weight:900;font-size:20px;line-height:1.5;padding:3px 12px;margin-bottom:6px;border-radius:4px}
.free-word{position:absolute;right:0;top:0;font-size:76px;font-weight:900;color:var(--green);line-height:1}
.free-sub{position:absolute;right:0;top:88px;font-size:11px;color:var(--muted);white-space:nowrap;text-align:right}
.warranty{left:470px;top:842px;width:400px;border:2px solid var(--green);border-radius:6px;overflow:hidden}
.warranty-title{background:var(--yellow);font-weight:900;font-size:17px;text-align:center;padding:2px 0;color:var(--green-dark)}
.warranty-body{font-size:11px;color:var(--muted);padding:4px 10px;line-height:1.45}

.voice{left:0;top:922px;width:900px;height:146px;background:var(--green-pale);border-top:4px solid var(--green)}
.voice-label{position:absolute;left:24px;top:14px;background:var(--orange);color:var(--white);font-weight:900;font-size:15px;padding:6px 10px;border-radius:4px}
.voice-card{position:absolute;top:14px;width:360px;display:flex;gap:10px}
.voice-card.one{left:130px}
.voice-card.two{left:512px}
.voice-face{width:70px;height:70px;flex:none;border-radius:50%;background:linear-gradient(#f3e3d0,#d8bfa3)}
.voice-name{font-weight:700;font-size:15px;margin-bottom:4px}
.voice-name small{font-weight:400;color:var(--muted);font-size:11px;margin-left:8px}
.voice-text{font-size:11px;color:var(--muted);line-height:1.55}

.footer{left:0;top:1068px;width:900px;height:132px;border-top:3px solid var(--green);padding:16px 28px}
.foot-brand{position:absolute;left:28px;top:14px;display:flex;align-items:center;gap:8px}
.foot-dot{width:34px;height:34px;border-radius:50%;background:var(--orange)}
.foot-name{font-family:"M PLUS Rounded 1c",sans-serif;font-weight:800;font-size:22px;color:var(--green)}
.foot-address{position:absolute;left:28px;top:62px;font-size:11px;color:var(--muted);line-height:1.5}
.foot-company{position:absolute;left:28px;top:100px;font-size:13px;font-weight:700}
.foot-msg{position:absolute;left:300px;top:18px;font-size:18px;font-weight:900;color:var(--green-dark)}
.foot-tel{position:absolute;left:300px;top:48px;display:flex;align-items:center;gap:8px;font-size:42px;font-weight:900;color:var(--green);letter-spacing:1px}
.foot-hours{position:absolute;left:740px;top:56px;font-size:11px;color:var(--muted);line-height:1.5}
.foot-url{position:absolute;left:300px;top:104px;font-size:14px;color:var(--text)}
</style>
</head>
<body>

<p class="abs eyebrow">家まで来てくれるメガネ屋さん</p>
<h1 class="abs brand">Lumo</h1>

<section class="abs safety">
  <p class="safety-title">万全のコロナ対策でお伺いします</p>
  <div class="safety-grid">
    <div class="safety-item"><div class="safety-icon" role="img" aria-label="マスク着用のアイコン"></div>マスク着用</div>
    <div class="safety-item"><div class="safety-icon" role="img" aria-label="手洗い消毒のアイコン"></div>手洗い・消毒</div>
    <div class="safety-item"><div class="safety-icon" role="img" aria-label="検温のアイコン"></div>検温</div>
    <div class="safety-item"><div class="safety-icon" role="img" aria-label="消毒の徹底のアイコン"></div>消毒の徹底</div>
    <div class="safety-item"><div class="safety-icon" role="img" aria-label="換気のアイコン"></div>定期的な換気</div>
  </div>
</section>

<div class="ph couple" role="img" aria-label="笑顔の高齢のご夫婦の写真"></div>
<div class="bubble call">お電話一本<br>どこでも<br>お伺いします</div>

<p class="abs lead">人の多い場所に外出しなくても大丈夫！<br>専用車でご自宅までお伺いします</p>
<div class="ph interior a" role="img" aria-label="専用車の車内 検査機器の写真"></div>
<div class="ph interior b" role="img" aria-label="専用車の車内 フレーム棚の写真"></div>

<svg class="abs band" viewBox="0 0 900 120" aria-hidden="true">
  <polygon points="0,70 900,0 900,120 0,120" fill="var(--green)"/>
</svg>
<div class="ph van" role="img" aria-label="出張用の白いワゴン車の写真"></div>
<div class="bubble eye">視力測定も<br>車内で<br>お手軽に</div>

<h2 class="abs headline">車内で視力検査を行い、<br>その場で、レンズ・フレームもお選びいただけます。</h2>

<div class="ph glasses" role="img" aria-label="緑のフレームのメガネの写真"></div>
<div class="bubble deliver">ご注文後、<br>お宅まで<br>お届けします</div>
<p class="abs lens-note">レンズメーカーは<b>KORU・SENAO</b>などの商品を扱っています。<br>男性用・女性用など各種取り揃えています。</p>

<section class="abs free">
  <ul class="free-list">
    <li>視力測定</li>
    <li>超音波洗浄</li>
    <li>ネジ・調整</li>
  </ul>
  <p class="free-word">無料</p>
  <p class="free-sub">メガネのことなら何でもご相談ください</p>
</section>
<section class="abs warranty">
  <p class="warranty-title">半年間の安心できる保証期間</p>
  <p class="warranty-body">お届けから半年間は度数の変更や破損に対応します。<br>見えにくい、合わないなど、お気軽にお申し付けください。</p>
</section>

<section class="abs voice">
  <p class="voice-label">お客様の声</p>
  <div class="voice-card one">
    <div class="voice-face" role="img" aria-label="お客様のイラスト"></div>
    <div>
      <p class="voice-name">長野市 A様<small>80代女性</small></p>
      <p class="voice-text">足が悪く外出が大変でしたが、家の前まで来てもらえて本当に助かりました。丁寧に測ってくれて、新しいメガネでよく見えます。</p>
    </div>
  </div>
  <div class="voice-card two">
    <div class="voice-face" role="img" aria-label="お客様のイラスト"></div>
    <div>
      <p class="voice-name">長野市 C様<small>70代男性</small></p>
      <p class="voice-text">車の中で検査もフレーム選びもできて驚きました。人混みに行かずに済むので安心です。調整も無料でありがたいです。</p>
    </div>
  </div>
</section>

<footer class="abs footer">
  <div class="foot-brand"><span class="foot-dot"></span><span class="foot-name">めがねのルモ</span></div>
  <p class="foot-address">〒380-0000<br>長野県みどり市本町1-2</p>
  <p class="foot-company">株式会社Lumo　TEL.000-000-4321</p>
  <p class="foot-msg">メガネのことなら何でもご相談ください！</p>
  <p class="foot-tel">
    <svg width="40" height="40" viewBox="0 0 24 24" aria-hidden="true"><path fill="var(--green)" d="M6.6 10.8a15.1 15.1 0 0 0 6.6 6.6l2.2-2.2a1 1 0 0 1 1-.25 11.4 11.4 0 0 0 3.6.57 1 1 0 0 1 1 1V20a1 1 0 0 1-1 1A17 17 0 0 1 3 4a1 1 0 0 1 1-1h3.5a1 1 0 0 1 1 1c0 1.25.2 2.45.57 3.570a1 1 0 0 1-.25 1z"/></svg>
    0120-00-4321
  </p>
  <p class="foot-hours">営業時間<br>9:00〜18:00</p>
  <p class="foot-url">http://www.lumo-megane.example</p>
</footer>

</body>
</html>
```